Harborline Stay Collective Business Card Design

Design a business card for Harborline Stay Collective. Look at the website for colors and reference. Card should have logo, name, title, office number, mobile number, email, URL and a tagline like, "Luxury Hotel & Resort Email Marketing" (This might change).

https://www.harborlinestaycollective.net

The rest I will leave up to your imagination.

Contact Information for Business Card

Logo, name, title, office number, mobile number, email, URL and a tagline like, "Luxury Hotel & Resort Email Marketing" (This might change).

```html
<!DOCTYPE html>
<html lang="en">
<head>
<meta charset="utf-8">
<title>Harborline Stay Collective – Business Card</title>
<link href="https://fonts.googleapis.com/css2?family=Arimo:wght@400;700&display=swap" rel="stylesheet">
<style>
  :root {
    --backdrop: #2b2b2d;
    --card-black: #060606;
    --card-white: #f5f5f6;
    --accent: #e86c0a;
    --ink: #111111;
    --muted: #6d6d6d;
    --rule: #c9c9c9;
  }
  * { margin: 0; padding: 0; box-sizing: border-box; }
  html, body { width: 1200px; height: 912px; overflow: hidden; }
  body {
    background: var(--backdrop);
    font-family: "Arimo", Arial, sans-serif;
    position: relative;
  }
  .card {
    position: absolute;
    width: 680px;
    height: 388px;
    border-radius: 22px;
    overflow: hidden;
  }
  /* Back side */
  .card--back {
    left: 90px;
    top: 48px;
    background: var(--card-black);
    color: #fff;
  }
  .brand-name {
    display: flex;
    align-items: center;
    gap: 14px;
    font-weight: 700;
    text-transform: uppercase;
    letter-spacing: 0.04em;
  }
  .brand-mark {
    width: 16px;
    height: 16px;
    background: var(--accent);
    flex: none;
  }
  .card--back .brand-name {
    position: absolute;
    left: 0; right: 0; top: 160px;
    justify-content: center;
    font-size: 36px;
    color: #fff;
  }
  .card--back .brand-mark { width: 22px; height: 22px; }
  .back-url {
    position: absolute;
    left: 0; right: 0; top: 282px;
    text-align: center;
    font-size: 17px;
    letter-spacing: 0.14em;
    color: #fff;
  }
  .back-url .domain { color: var(--accent); }

  /* Front side */
  .card--front {
    left: 430px;
    top: 472px;
    background: var(--card-white);
    color: var(--ink);
  }
  .card--front .brand-name {
    position: absolute;
    left: 44px;
    top: 186px;
    width: 260px;
    font-size: 20px;
    line-height: 1.2;
    color: var(--ink);
    align-items: flex-start;
  }
  .card--front .brand-mark { margin-top: 4px; }
  .divider {
    position: absolute;
    left: 330px;
    top: 70px;
    width: 1px;
    height: 230px;
    background: var(--rule);
  }
  .contact {
    position: absolute;
    left: 356px;
    top: 86px;
  }
  .person-name { font-size: 26px; font-weight: 700; }
  .person-title { font-size: 17px; color: var(--muted); margin-top: 2px; }
  .contact-list { list-style: none; margin-top: 20px; }
  .contact-list li {
    display: flex;
    align-items: center;
    gap: 10px;
    font-size: 15.5px;
    line-height: 24px;
    color: var(--ink);
  }
  .contact-list svg { width: 14px; height: 14px; flex: none; }
  .tagline-band {
    position: absolute;
    left: 0; bottom: 0;
    width: 530px;
    height: 44px;
    background: var(--accent);
    color: #fff;
    font-size: 18px;
    padding-left: 36px;
    display: flex;
    align-items: center;
  }
  .band-end {
    position: absolute;
    right: 0; bottom: 0;
    width: 150px;
    height: 56px;
    background: var(--card-black);
  }
</style>
</head>
<body>

<section class="card card--back" aria-label="Card back">
  <div class="brand-name"><span class="brand-mark"></span>Harborline Stay Collective</div>
  <p class="back-url">www.<span class="domain">harborlinestaycollective</span>.net</p>
</section>

<section class="card card--front" aria-label="Card front">
  <div class="brand-name"><span class="brand-mark"></span>Harborline Stay Collective</div>
  <div class="divider"></div>
  <div class="contact">
    <p class="person-name">Daniel Reyes</p>
    <p class="person-title">President</p>
    <ul class="contact-list">
      <li>
        <svg viewBox="0 0 16 16" aria-hidden="true"><path fill="#e86c0a" d="M3.5 1.5l2.5 0 1 3.5-1.6 1.2a8 8 0 0 0 4.4 4.4L11 9l3.5 1v2.5c0 1-1 2-2 2A11 11 0 0 1 1.5 3.5c0-1 1-2 2-2z"/></svg>
        555.014.2000
      </li>
      <li>
        <svg viewBox="0 0 16 16" aria-hidden="true"><rect x="4" y="1" width="8" height="14" rx="1.5" fill="none" stroke="#e86c0a" stroke-width="1.8"/><circle cx="8" cy="12.3" r="0.9" fill="#e86c0a"/></svg>
        555.014.2001
      </li>
      <li>
        <svg viewBox="0 0 16 16" aria-hidden="true"><rect x="1" y="3" width="14" height="10" fill="#e86c0a"/><path d="M1.5 3.5l6.5 5 6.5-5" fill="none" stroke="#fff" stroke-width="1.3"/></svg>
        info@harborlinestaycollective.net
      </li>
      <li>
        <svg viewBox="0 0 16 16" aria-hidden="true"><circle cx="8" cy="8" r="7" fill="#e86c0a"/><ellipse cx="8" cy="8" rx="3" ry="7" fill="none" stroke="#fff" stroke-width="1"/><path d="M1 8h14" stroke="#fff" stroke-width="1"/></svg>
        www.harborlinestaycollective.net
      </li>
    </ul>
  </div>
  <div class="tagline-band">Luxury Hotel &amp; Resort Email Marketing</div>
  <div class="band-end"></div>
</section>

</body>
</html>
```